Professional Baby Bottle Bank Print Design

We need a baby bottle design that is 4.25" wide x 2.28" tall with a maximum of 6 colors (white is counted as a color).

The bottle design needs to be fun but professional. Bottles with cartoon images on it will be rejected immediately.

The bottle design wraps around the bottle. See examples here: https://wendrix.net/cat/BabyBottles/OrvelJarsKit/5

Minimum font size is 10pt.

The bottle design must have the following text on it:
Main Text: Love them both
Paragraph text: Our ministry’s aim is to not only save unborn babies, but to provide love, support, and life-saving resources for vulnerable women in our community. By filling this bottle with cash, checks, and spare coins and returning it on collection day, you are truly saving and changing lives!
Optional text: Thank you!

We are including an example file and a template file. You do NOT have to use the template - but your file has to be the exact size mentioned. If you don't design as well as our sample, please don't waste our time by spamming us with hundreds of designs. We will ban design houses that spam us with designs that are more layouts (and not well designed).

Please note - white is a color. You don't have to do a box - but anything you don't make white will be see-through.

We will take the winners of this contest to a survey with the customers. We may choose two and edit the text of one slightly to be different. We must know the fonts used.

No gradients unless they are half-toned with relatively big sized dots.

Target Market(s)

Church Attendees coming from a Pregnancy Center

Industry/Entity Type

Religious Christian Churches

Requirements
Must have
• Professional, great palette, wording as described.
Nice to have
• Integrated design across the whole space with areas for text (no text all the way across)
Should not have
• Cartoon figures; elements shoved together that don't go together (i.e. - actually design something)

```html
<!DOCTYPE html>
<html lang="en">
<head>
<meta charset="utf-8">
<title>Love Them Both – Baby Bottle Label</title>
<link href="https://fonts.googleapis.com/css2?family=Fraunces:opsz,wght@144,900&family=Manrope:wght@400;500&family=Playfair+Display:ital,wght@1,500&display=swap" rel="stylesheet">
<style>
  :root {
    --page: #ecc8e0;
    --label: #cf4b9d;
    --label-deep: #b03c86;
    --lavender: #a7a3d6;
    --mauve: #c07cb8;
    --white: #ffffff;
    --petal: #fbe9f4;
    --figure: #a8bde2;
    --wave: #d863ab;
  }
  html, body {
    margin: 0;
    width: 1200px;
    height: 1200px;
    overflow: hidden;
    background: var(--page);
  }
  .bottle-label {
    position: absolute;
    left: 40px;
    top: 300px;
    width: 1120px;
    height: 600px;
    background: var(--label);
    overflow: hidden;
  }
  .bubble {
    position: absolute;
    border-radius: 50%;
  }
  .bubble--mauve { left: 60px; top: -100px; width: 200px; height: 200px; background: var(--mauve); }
  .bubble--lavender { left: -40px; top: -40px; width: 210px; height: 210px; background: var(--lavender); }
  .bubble--rose { left: -10px; top: 40px; width: 170px; height: 170px; background: var(--mauve); opacity: .7; }

  .wave-field {
    position: absolute;
    left: 0;
    top: 300px;
    width: 560px;
    height: 300px;
    background: var(--wave);
    border-radius: 0 100% 0 0 / 0 100% 0 0;
    opacity: .6;
  }
  .wave-field--right {
    left: auto;
    right: 0;
    top: 360px;
    width: 260px;
    height: 240px;
    border-radius: 100% 0 0 0 / 100% 0 0 0;
    opacity: .45;
  }
  .corner-fold {
    position: absolute;
    left: 0;
    bottom: 0;
  }
  .daisy {
    position: absolute;
    border-radius: 50%;
    background: var(--petal);
  }
  .daisy--large { left: 268px; top: -40px; width: 190px; height: 190px; }
  .daisy--mid { left: 40px; top: 60px; width: 130px; height: 130px; }
  .daisy--small { left: 471px; top: 115px; width: 40px; height: 40px; }
  .daisy--corner { left: 1030px; top: -40px; width: 96px; height: 96px; }

  .mother-figure {
    position: absolute;
    left: 35px;
    top: 36px;
    width: 325px;
    height: 300px;
    border-radius: 46% 46% 8% 8%;
    background: var(--figure);
  }
  .headline {
    position: absolute;
    left: 96px;
    top: 292px;
    width: 330px;
    margin: 0;
    font-family: "Fraunces", Georgia, serif;
    font-weight: 900;
    font-size: 102px;
    line-height: 90px;
    letter-spacing: -3px;
    text-align center;
    text-align: center;
    color: var(--white);
    text-shadow: 4px 4px 0 var(--label-deep);
  }
  .mission {
    position: absolute;
    right: 77px;
    top: 80px;
    width: 680px;
    margin: 0;
    font-family: "Manrope", Arial, sans-serif;
    font-weight: 500;
    font-size: 37px;
    line-height: 36.5px;
    letter-spacing: -0.3px;
    text-align: right;
    color: var(--white);
  }
  .thanks {
    position: absolute;
    left: 674px;
    top: 480px;
    width: 280px;
    margin: 0;
    text-align: center;
    font-family: "Playfair Display", Georgia, serif;
    font-style: italic;
    font-weight: 500;
    font-size: 48px;
    line-height: 1;
    color: var(--petal);
  }
</style>
</head>
<body>
  <main class="bottle-label">
    <div class="bubble bubble--mauve"></div>
    <div class="bubble bubble--lavender"></div>
    <div class="bubble bubble--rose"></div>

    <div class="wave-field" role="img" aria-label="Fine flowing white line pattern"></div>
    <div class="wave-field wave-field--right" role="img" aria-label="Fine flowing white line pattern"></div>

    <svg class="corner-fold" width="100" height="80" viewBox="0 0 100 80" aria-hidden="true">
      <polygon points="0,8 100,80 0,80" fill="#ffffff"/>
    </svg>

    <div class="daisy daisy--mid" role="img" aria-label="White daisy flower"></div>
    <div class="daisy daisy--large" role="img" aria-label="White daisy flower"></div>
    <div class="daisy daisy--small" role="img" aria-label="Small white daisy flower"></div>
    <div class="daisy daisy--corner" role="img" aria-label="White daisy flower"></div>

    <div class="mother-figure" role="img" aria-label="Illustration of a red-haired mother in a blue top holding her newborn baby"></div>

    <h1 class="headline">Love them both</h1>

    <p class="mission">Our ministry’s aim is to not only<br>save unborn babies<br>but to provide love, support<br>and life-saving resources<br>for vulnerable women in our<br>community. By filling<br>this bottle with cash, checks<br>and spare coins and returning it on<br>collection day, you are<br>truly saving and changing lives!</p>

    <p class="thanks">Thank you!</p>
  </main>
</body>
</html>
```